Rain On Every Quiet Street - Tom Hallowell - CD Cover Design Project

Single Cover for CD & Online media e.g. SongVault Graphics

The first Album release from Tom Hallowell will be Titled 'Rain On Every Quiet Street'.

For the release the Album requires artwork that is eye catching, seriously professional & meets the requirements of Disc Harbor, SongVault and also a physical copy on CD.

see details in this link:
http://members.discharbor-example.com/faq.aspx
http://selfmadesound.discharbor-example.com/2009/11/avoid-album-art-atrocities/
http://replies.quibbla-example.com/question/index?qid=20111015141433AAdDTmH

Please find all files you need to get started and a mini mix of the album tracks in this drop box
https://www.filecrate-example.com/sh/k8w4nrtavbzqmu2/7yLpQ5dKd

Any advice on this would be greatly appreciated,

I would also like the two logo's I have uploaded to be used,
one is the Tom Hallowell logo and the other is for Whitmore & Doyle Records logo (please remove the R and replace with a C for copyright.)

I would like the Tom Hallowell logo to feature a heart instead of the tie.

I have uploaded pictures of Tom Hallowell and another zip file of many others, it would be nice to include one of these maybe on the 2nd page or back of the CD. Please don't use them as the front cover.

I would like the cover layout to be similar layout to the previous Single cover for 'Every Lamp Went Dark Tonight'. Bar of colour down the side featuring the Tom Hallowell logo and title below with picture to the side. I am open to new ideas for the layout but want to create some unity to make the artists and his work easily recognizable

If you submit a design please don't delete the raw file ideas as I may ask you to revert to one of these ideas.

Good Luck
Updates

I would proffer an illustrated design 

Please leave the Whitmore & Doyle Logo off the front cover, (should be on the back of the CD cover)

I have uploaded the previous CD's cover layout to help show what I am looking for, some of the covers are looking very good, please remember illustrated covers proffered. 

Industry/Entity Type

Artists

```html
<!DOCTYPE html>
<html lang="en">
<head>
<meta charset="utf-8">
<title>Tom Hallowell – Rain On Every Quiet Street</title>
<link rel="stylesheet" href="https://fonts.googleapis.com/css2?family=Bebas+Neue&display=swap">
<style>
  :root {
    --backdrop: #f1f1f1;
    --accent-yellow: #f2ee1c;
    --photo-warm: #c79a6a;
    --photo-light: #d9c2a0;
    --photo-dark: #2a1e18;
    --photo-mid: #5a3d2c;
  }
  * { margin: 0; padding: 0; box-sizing: border-box; }
  html, body {
    width: 1200px;
    height: 925px;
    overflow: hidden;
    background: var(--backdrop);
  }
  .stage {
    position: relative;
    width: 1200px;
    height: 925px;
  }
  .album-cover {
    position: absolute;
    left: 230px;
    top: 125px;
    width: 740px;
    height: 675px;
    overflow: hidden;
  }
  .cover-photo {
    position: absolute;
    inset: 0;
    background:
      radial-gradient(ellipse 45% 40% at 38% 22%, var(--photo-light) 0%, rgba(217,194,160,0) 70%),
      radial-gradient(ellipse 60% 55% at 45% 85%, var(--photo-dark) 0%, rgba(42,30,24,0.6) 55%, rgba(42,30,24,0) 85%),
      linear-gradient(120deg, var(--photo-mid) 0%, var(--photo-warm) 45%, var(--photo-light) 70%, #8a7a6a 100%);
  }
  .cover-type {
    position: absolute;
    inset: 0;
    width: 740px;
    height: 675px;
  }
  .artist-name {
    font-family: 'Bebas Neue', sans-serif;
    font-size: 130px;
    fill: var(--accent-yellow);
  }
  .release-title {
    font-family: 'Bebas Neue', sans-serif;
    font-size: 24px;
    fill: var(--photo-dark);
  }
  .title-bar { fill: var(--accent-yellow); }
</style>
</head>
<body>
  <main class="stage">
    <section class="album-cover">
      <div class="cover-photo" role="img" aria-label="Warm-toned photo of the artist in sunglasses and a dark leather jacket holding a cream rotary telephone"></div>
      <svg class="cover-type" viewBox="0 0 740 675" aria-label="Tom Hallowell – Rain On Every Quiet Street">
        <g transform="translate(114 575) rotate(-25.6)">
          <text class="artist-name" x="8" y="-34" textLength="640" lengthAdjust="spacingAndGlyphs">TOM HALLOWELL</text>
          <text class="release-title" x="395" y="-7" textLength="260" lengthAdjust="spacingAndGlyphs">RAIN ON EVERY QUIET STREET</text>
          <rect class="title-bar" x="0" y="0" width="662" height="15"/>
        </g>
      </svg>
    </section>
  </main>
</body>
</html>
```